Exciting Personal Development Book Cover: FIND ZEN NOW!

Design a Book Cover for my personal development book.
Title: Find Zen Now!
Author: Marcus Telly
Tagline: A real-life solution to get unstuck and break free

My picture must make up the front cover as I need to build my brand and people should recognise me on book shelves. Bold and catchy. How you do it is up to you. There must be space for a short testimonial from a famous person who is currently reading my book. I uploaded a sample of what I made in Photoshop but I don't have design skills.

I've added a PDF of my book so you can read the chapter index and introduction to get a sense of the content.

Target Market(s)

Personal Development Self-Help Market

Industry/Entity Type

Personal Development

Font styles to use
Serif
Sans Serif

Requirements
Must have
• My picture as hero image on cover.
Nice to have
• Must have Title, Tagline and my author name. If possible ZEN stands for 'Zeal, Energy & Nerve' If there is a way to fit this somewhere great. If it's too much then it can go somewhere on the back.

```html
<!DOCTYPE html>
<html lang="en">
<head>
<meta charset="utf-8">
<title>Find Zen Now! — Book Cover</title>
<link href="https://fonts.googleapis.com/css2?family=Bebas+Neue&display=swap" rel="stylesheet">
<style>
  :root {
    --page-bg: #ececec;
    --navy-deep: #1c3473;
    --navy-mid: #2a55a0;
    --accent-blue: #00a0e3;
    --ink-navy: #1d2f6f;
    --white: #ffffff;
    --paper: #f6f6f8;
  }
  html, body {
    margin: 0;
    padding: 0;
    width: 1200px;
    height: 1200px;
    overflow: hidden;
    background: var(--page-bg);
  }
  .cover {
    position: absolute;
    left: 238px;
    top: 81px;
    width: 683px;
    height: 1024px;
    overflow: hidden;
    background: radial-gradient(ellipse 70% 55% at 62% 52%, var(--navy-mid) 0%, #23468c 45%, var(--navy-deep) 100%);
    font-family: "Bebas Neue", "Arial Narrow", sans-serif;
  }
  .author-photo {
    position: absolute;
    left: 0;
    top: 0;
    width: 683px;
    height: 1024px;
  }
  .title {
    position: absolute;
    left: 64px;
    top: 45px;
    margin: 0;
    font-weight: 400;
    font-size: 262px;
    line-height: 228px;
    color: var(--white);
    z-index: 2;
  }
  .title-line {
    display: block;
    width: max-content;
    transform-origin: left center;
  }
  .title-line.first { transform: scaleX(0.84); }
  .title-line.accent { color: var(--accent-blue); transform: scaleX(0.93); }
  .title-line.last { transform: scaleX(0.62); }
  .author-name {
    position: absolute;
    left: 64px;
    top: 722px;
    margin: 0;
    font-size: 90px;
    line-height: 97px;
    font-weight: 400;
    color: var(--white);
    z-index: 2;
  }
  .author-name span { display: block; }
  .testimonial {
    position: absolute;
    left: 392px;
    top: 44px;
    width: 270px;
    z-index: 2;
  }
  .testimonial-mark {
    font-family: Georgia, "Times New Roman", serif;
    font-weight: 700;
    color: var(--white);
    line-height: 1;
  }
  .testimonial-mark.open {
    position: absolute;
    left: 0;
    top: -6px;
    font-size: 62px;
  }
  .testimonial-text {
    margin: 0 0 0 38px;
    font-size: 32px;
    line-height: 38px;
    color: var(--white);
  }
  .testimonial-text .accent { color: var(--accent-blue); }
  .testimonial-mark.close {
    display: inline-block;
    font-size: 62px;
    line-height: 0;
    vertical-align: -30px;
    margin-left: 16px;
  }
  .tagline-band {
    position: absolute;
    left: 0;
    bottom: 0;
    width: 683px;
    height: 100px;
    z-index: 3;
  }
  .tagline-band svg { position: absolute; left: 0; top: 0; }
  .tagline {
    position: absolute;
    left: 0;
    right: 0;
    top: 34px;
    margin: 0;
    text-align: center;
    font-size: 35px;
    line-height: 1;
    color: var(--ink-navy);
    letter-spacing: 0.3px;
  }
</style>
</head>
<body>
  <main class="cover">
    <svg class="author-photo" viewBox="0 0 683 1024" role="img" aria-label="Portrait photo of the author smiling in a white shirt with tattooed forearms">
      <defs>
        <linearGradient id="photoTone" x1="0" y1="0" x2="0" y2="1">
          <stop offset="0.16" stop-color="#3a3434"/>
          <stop offset="0.24" stop-color="#b98a72"/>
          <stop offset="0.42" stop-color="#c79c84"/>
          <stop offset="0.48" stop-color="#eeeef2"/>
          <stop offset="1" stop-color="#e4e2e6"/>
        </linearGradient>
      </defs>
      <path fill="url(#photoTone)" d="M442 300 C440 210 490 172 545 172 C600 172 628 215 628 300 L630 430 C660 445 683 455 683 465 L683 964 L365 964 L352 760 C346 620 352 540 395 505 C420 485 450 470 455 440 C448 400 444 350 442 300 Z"/>
    </svg>

    <h1 class="title">
      <span class="title-line first">FIND</span>
      <span class="title-line accent">ZEN</span>
      <span class="title-line last">NOW!</span>
    </h1>

    <aside class="testimonial">
      <span class="testimonial-mark open">“</span>
      <p class="testimonial-text"><span class="accent">ZEN</span> STANDS FOR<br>'ZEAL, ENERGY<br>&amp; NERVE'<span class="testimonial-mark close">”</span></p>
    </aside>

    <h2 class="author-name"><span>MARCUS</span><span>TELLY</span></h2>

    <footer class="tagline-band">
      <svg width="683" height="100" viewBox="0 0 683 100" aria-hidden="true">
        <path fill="var(--paper)" d="M0 14 L18 10 L34 13 L52 8 L70 12 L92 9 L112 13 L130 7 L150 11 L172 8 L196 12 L214 6 L236 10 L258 7 L280 12 L302 8 L322 11 L346 6 L368 10 L390 7 L414 12 L436 8 L458 11 L480 6 L502 10 L526 7 L548 12 L570 8 L592 11 L616 7 L638 12 L660 9 L683 12 L683 100 L0 100 Z"/>
      </svg>
      <p class="tagline">A REAL-LIFE SOLUTION TO GET UNSTUCK AND BREAK FREE</p>
    </footer>
  </main>
</body>
</html>
```